Business card design needed

Double sided
Color, unique, elegant

Maybe put this quote somewhere?? But I think it might make it to cluttered?
“The Pilates Method of Body
Conditioning develops the body
uniformly, corrects posture, restores
vitality, invigorates the mind and
elevates the spirit”
- Henrik Dovacombe

Industry/Entity Type

Business

Contact Information for Business Card

Marta Kellbrook
Pilates Instructor & Personal trainer
Mobile: 0498265043
www.lorvix.com.au
email: lorvixhealth.fitness@qentamail.com

```html
<!DOCTYPE html>
<html lang="en">
<head>
<meta charset="utf-8">
<title>Lorvix Health and Fitness — Business Card</title>
<link rel="stylesheet" href="https://fonts.googleapis.com/css2?family=Caveat:wght@500&family=Questrial&family=Tinos:ital,wght@0,400;1,700&display=swap">
<style>
  :root {
    --bg: #e6e6e8;
    --card: #ffffff;
    --green: #8cc56b;
    --purple: #a466b3;
    --purple-dark: #8e4f9e;
    --ink: #4a4a4a;
    --photo-a: #d9d2c9;
    --photo-b: #f1ece6;
  }
  * { box-sizing: border-box; margin: 0; padding: 0; }
  html, body { width: 1200px; height: 800px; overflow: hidden; }
  body { background: var(--bg); position: relative; font-family: "Tinos", serif; }

  .card {
    position: absolute; top: 250px; width: 520px; height: 300px;
    background: var(--card); overflow: hidden;
    box-shadow: 0 6px 18px rgba(0,0,0,.18);
  }
  .card--quote { left: 50px; }
  .card--contact { left: 630px; }
  .card__band { position: absolute; left: 0; right: 0; height: 14px; }
  .card__band--top { top: 0; background: var(--green); }
  .card__band--bottom { bottom: 0; background: var(--purple); }

  .brand { position: absolute; display: flex; align-items: center; gap: 8px;
    font-family: "Questrial", sans-serif; color: var(--ink); }
  .brand__dot { width: 14px; height: 14px; border-radius: 50%; background: var(--green); flex: none; }
  .brand__name { font-size: 20px; line-height: 1.15; }

  /* quote side */
  .card--quote .brand { left: 30px; top: 128px; width: 160px; }
  .divider { position: absolute; left: 204px; top: 40px; width: 2px; height: 220px; background: var(--purple); }
  .quote { position: absolute; left: 224px; top: 38px; width: 270px; height: 220px; }
  .quote__bubble { position: absolute; inset: 0; }
  .quote__text { position: absolute; left: 22px; top: 22px; width: 226px;
    font-size: 14px; line-height: 1.45; color: var(--purple-dark); text-align: center; }
  .quote__author { position: absolute; right: 60px; bottom: 16px;
    font-family: "Caveat", cursive; font-size: 22px; color: var(--purple-dark); }

  /* contact side */
  .frame { position: absolute; border: 1.5px solid var(--purple); border-radius: 12px; background: var(--card); }
  .frame--logo { left: 36px; top: 52px; width: 150px; height: 112px; }
  .frame--logo .brand { left: 14px; top: 38px; }
  .frame--photo { padding: 8px; }
  .frame--photo-weights { left: 270px; top: 30px; width: 150px; height: 118px; }
  .frame--photo-plank { left: 330px; top: 140px; width: 150px; height: 104px; }
  .photo { width: 100%; height: 100%; border-radius: 6px;
    background: linear-gradient(135deg, var(--photo-b), var(--photo-a)); }

  .person { position: absolute; left: 36px; top: 176px; }
  .person__name { font-size: 26px; font-weight: 700; font-style: italic; color: var(--purple); }
  .person__role { font-size: 12px; font-weight: 700; color: var(--green); margin-top: 2px; }

  .contacts { position: absolute; left: 36px; top: 226px; list-style: none; }
  .contacts__item { display: flex; align-items: center; gap: 8px; height: 18px;
    font-size: 11px; color: var(--ink); }
  .contacts__icon { width: 14px; height: 14px; border-radius: 2px; background: var(--purple); flex: none; }
</style>
</head>
<body>

<section class="card card--quote" aria-label="Card back">
  <div class="card__band card__band--top"></div>
  <div class="brand">
    <span class="brand__dot"></span>
    <span class="brand__name">Lorvix Health and Fitness</span>
  </div>
  <div class="divider"></div>
  <figure class="quote">
    <svg class="quote__bubble" viewBox="0 0 270 220" width="270" height="220" aria-hidden="true">
      <path d="M16 2 H254 A14 14 0 0 1 268 16 V170 A14 14 0 0 1 254 184 H236 L244 214 L214 184 H16 A14 14 0 0 1 2 170 V16 A14 14 0 0 1 16 2 Z"
            fill="none" stroke="#a466b3" stroke-width="1.5"/>
    </svg>
    <blockquote class="quote__text">“The Pilates Method of Body Conditioning develops the body uniformly, corrects posture, restores vitality, invigorates the mind and elevates the spirit”</blockquote>
    <figcaption class="quote__author">Henrik Dovacombe</figcaption>
  </figure>
  <div class="card__band card__band--bottom"></div>
</section>

<section class="card card--contact" aria-label="Card front">
  <div class="card__band card__band--top"></div>
  <div class="frame frame--logo">
    <div class="brand">
      <span class="brand__dot"></span>
      <span class="brand__name">Lorvix</span>
    </div>
  </div>
  <div class="frame frame--photo frame--photo-weights">
    <div class="photo" role="img" aria-label="Photo of a woman training with hand weights"></div>
  </div>
  <div class="frame frame--photo frame--photo-plank">
    <div class="photo" role="img" aria-label="Photo of a woman in a side plank pose"></div>
  </div>
  <div class="person">
    <p class="person__name">Marta Kellbrook</p>
    <p class="person__role">Pilates Instructor &amp; Personal trainer</p>
  </div>
  <ul class="contacts">
    <li class="contacts__item">
      <svg class="contacts__icon" viewBox="0 0 14 14" aria-hidden="true"><path d="M4 3 L6 5 L5 6.5 Q6 8.5 7.5 9 L9 8 L11 10 L10 11.5 Q5.5 11.5 2.5 4.5 Z" fill="#fff"/></svg>
      <span>0498265043</span>
    </li>
    <li class="contacts__item">
      <svg class="contacts__icon" viewBox="0 0 14 14" aria-hidden="true"><rect x="2.5" y="4" width="9" height="6.5" fill="none" stroke="#fff" stroke-width="1"/><path d="M2.5 4 L7 8 L11.5 4" fill="none" stroke="#fff" stroke-width="1"/></svg>
      <span>lorvixhealth.fitness@qentamail.com</span>
    </li>
    <li class="contacts__item">
      <svg class="contacts__icon" viewBox="0 0 14 14" aria-hidden="true"><circle cx="7" cy="7" r="4.5" fill="none" stroke="#fff" stroke-width="1"/><ellipse cx="7" cy="7" rx="2" ry="4.5" fill="none" stroke="#fff" stroke-width="0.8"/><path d="M2.5 7 H11.5" stroke="#fff" stroke-width="0.8"/></svg>
      <span>www.lorvix.com.au</span>
    </li>
  </ul>
  <div class="card__band card__band--bottom"></div>
</section>

</body>
</html>
```